Best Seller Book Cover ...

Book Title: Stop Chasing Meaning: Pick a Trail, Keep to That Trail, Mind the Geese

Edgy, Minimalist, Compelling, Attractive, Classy design.

Very clean. See examples.,

Target Market(s)

Mid Life People ages 38-55 Male and Female equally

Requirements

Nice to have
• Nice to Have:

Minimalist and eye catching ( i have loaded a few examples of what this means)
Should not have
• Clip Art
Clutter

```html
<!DOCTYPE html>
<html lang="en">
<head>
<meta charset="utf-8">
<title>Stop Chasing Meaning — Book Cover</title>
<link rel="stylesheet" href="https://fonts.googleapis.com/css2?family=Oswald:wght@300;700&display=swap">
<style>
  :root {
    --paper: #ffffff;
    --road: #6b6c6e;
    --shoulder: #dcdcdc;
    --paint: #ffffff;
    --accent: #c8373a;
  }
  html, body {
    margin: 0;
    padding: 0;
    overflow: hidden;
    background: var(--paper);
  }
  .cover {
    position: relative;
    width: 800px;
    height: 1200px;
    background: var(--paper);
    overflow: hidden;
  }
  .road-art {
    position: absolute;
    inset: 0;
  }
  .title {
    position: absolute;
    left: 192px;
    top: 44px;
    width: 416px;
    margin: 0;
    text-align: center;
    color: var(--paint);
    font-family: "Oswald", "Arial Narrow", sans-serif;
    font-weight: 300;
  }
  .title span { display: block; }
  .title__kicker {
    font-weight: 700;
    font-size: 46px;
    line-height: 44px;
    text-transform: uppercase;
    letter-spacing: 0.5px;
  }
  .title__kicker + .title__small { margin-top: 8px; }
  .title__small {
    font-size: 44px;
    line-height: 46px;
    letter-spacing: 0.5px;
  }
  .title__big {
    font-weight: 700;
    font-size: 122px;
    line-height: 118px;
    margin-top: -4px;
  }
</style>
</head>
<body>
  <main class="cover">
    <svg class="road-art" width="800" height="1200" viewBox="0 0 800 1200" aria-hidden="false">
      <rect class="shoulder" x="165" y="0" width="470" height="1200" fill="var(--shoulder)"/>
      <rect class="asphalt" x="192" y="0" width="416" height="1200" fill="var(--road)"/>
      <rect class="antlers" role="img" aria-label="Red deer antlers spreading across the road"
            x="14" y="722" width="772" height="270" rx="40" fill="var(--accent)"/>
      <g class="lane-dashes" fill="var(--paint)">
        <rect x="381" y="716" width="38" height="90"/>
        <rect x="381" y="908" width="38" height="92"/>
        <rect x="381" y="1094" width="38" height="106"/>
      </g>
    </svg>

    <h1 class="title">
      <span class="title__kicker">Stop Chasing</span>
      <span class="title__kicker">Meaning:</span>
      <span class="title__small">Pick a</span>
      <span class="title__big">Trail</span>
      <span class="title__small">Keep to That</span>
      <span class="title__big">Trail</span>
      <span class="title__small">Mind the</span>
      <span class="title__big">Geese</span>
    </h1>
  </main>
</body>
</html>
```